A5 Flyer for Window Cleaning Company

2 sided Flyer design required for window cleaning company. One side to include we use traditional and hot water fed pole window cleaning systems, conservatory cleaning, and fascia and soffit cleaning. The other side to be for Gutter cleaning. See the must haves section of project brief for more info. Mixture of some images and text for both sides. ( do not have to use all images supplied). The flyer will be used to promote the business to new residential customers.

Target Market(s)

Private households/new customers

Industry/Entity Type

Window Cleaning

Font styles to use
Serif

Requirements
Must have
• Company address ( 7 Old Pennick Court Harlow Street Edinburgh EH4 9RQ
Phone numbers( 0131 482 7719 0800 061 2287).
Website and email address ( info@falconbright-cleaning.example)
Excellent Customer Service. Competitive prices. Established 1994.
Side 1of flyer = Falconbright Window Cleaning Side 2 of flyer Falconbright Gutter Cleaning.
Nice to have
• Professional look.

```html
<!DOCTYPE html>
<html lang="en">
<head>
<meta charset="utf-8">
<title>Falconbright Cleaning Flyers</title>
<link href="https://fonts.googleapis.com/css2?family=Libre+Baskerville:wght@400;700&family=Source+Serif+4:wght@400;600&display=swap" rel="stylesheet">
<style>
:root{
  --navy:#312d63;
  --sky:#83aedf;
  --sky-soft:#a9c7ea;
  --white:#ffffff;
  --stage:#747474;
  --ink:#2c2a4a;
  --photo-sky:#8fa9c8;
  --photo-wall:#5d5450;
  --photo-glass:#7d8791;
  --photo-red:#8a4b4f;
}
*{box-sizing:border-box;margin:0;padding:0}
html,body{width:1200px;height:849px;overflow:hidden}
body{background:var(--stage);position:relative;font-family:"Source Serif 4",serif;color:var(--ink)}
.flyer{position:absolute;top:94px;width:464px;height:664px;background:var(--white);overflow:hidden;box-shadow:4px 5px 8px rgba(0,0,0,.35)}
.flyer--gutter{left:96px}
.flyer--window{left:605px}
.hero-photo{position:absolute;left:0;top:0;width:464px;height:386px}
.flyer--gutter .hero-photo{background:linear-gradient(100deg,var(--photo-sky) 0%,var(--photo-sky) 35%,var(--photo-wall) 60%,#4a4340 100%)}
.flyer--window .hero-photo{background:linear-gradient(100deg,var(--photo-glass) 0%,#a7adb3 40%,var(--photo-red) 62%,#6f757b 100%)}
.roof{position:absolute;left:0;top:0;width:464px;height:386px}
.brand{position:absolute;top:60px;display:flex;align-items:center;gap:5px}
.flyer--gutter .brand{right:18px}
.flyer--window .brand{left:18px}
.brand-mark{width:12px;height:12px;background:var(--sky)}
.brand-name{font-family:"Libre Baskerville",serif;font-weight:700;font-size:12px;color:var(--white);letter-spacing:.5px}
.headline{position:absolute;left:0;width:464px;top:280px;text-align:center;font-family:"Libre Baskerville",serif;font-weight:700;color:var(--navy);line-height:1}
.headline .line-top{display:block;font-size:19px;letter-spacing:.5px}
.headline .line-main{display:block;font-size:38px;margin-top:4px;letter-spacing:1px}
.headline .line-bottom{display:block;font-size:21px;margin-top:4px;letter-spacing:.5px}
.intro{position:absolute;left:20px;width:424px;top:384px;text-align:center;font-size:8.4px;line-height:1.25}
.services-title{position:absolute;left:30px;top:424px;font-size:18px;font-weight:400;color:var(--navy);letter-spacing:.3px}
.services-list{position:absolute;left:30px;top:452px;list-style:none}
.services-list li{font-size:9.5px;height:13.6px;display:flex;align-items:center;gap:8px}
.services-list svg{width:5px;height:7px}
.photo-frame{position:absolute;border:1px solid var(--sky);padding:2px;background:var(--white)}
.photo-frame div{width:100%;height:100%}
.frame-a{left:176px;top:427px;width:146px;height:87px}
.frame-b{left:289px;top:464px;width:144px;height:87px}
.flyer--gutter .frame-a div{background:linear-gradient(120deg,#6f6a66,#c48a4a 50%,#d9dde2)}
.flyer--gutter .frame-b div{background:linear-gradient(160deg,#cfd6dd,#eef0f2 55%,#b84250 70%,#3d3f44)}
.flyer--window .frame-a div{background:linear-gradient(90deg,#6d97c9 0%,#6d97c9 32%,#9a5a3d 33%,#b06a48 62%,#c9d2da 63%,#dfe5ea 100%)}
.flyer--window .frame-b div{background:linear-gradient(120deg,#c7d3dc,#e6ebef 45%,#2f5f9e 70%,#7a8a66)}
.strapline{position:absolute;left:31px;top:566px;display:flex;gap:2px}
.strapline span{background:var(--sky);transform:skewX(-18deg);padding:2px 5px;font-family:"Libre Baskerville",serif;font-weight:700;font-size:10.3px;color:var(--navy);white-space:nowrap}
.strapline b{display:inline-block;transform:skewX(18deg);font-weight:700}
.contact{position:absolute;left:0;top:587px;width:464px;height:77px;background:var(--sky);display:flex;flex-direction:column;align-items:center;padding-top:7px;gap:2.5px}
.contact p{display:flex;align-items:center;gap:6px;font-size:9.3px;color:var(--navy);letter-spacing:.2px;height:12px}
.contact svg{width:9px;height:9px}
.contact .phones{font-weight:600}
</style>
</head>
<body>

<!-- Gutter side -->
<section class="flyer flyer--gutter">
  <div class="hero-photo" role="img" aria-label="Photo of a worker on a ladder clearing a house gutter with a long pole against a blue sky"></div>
  <svg class="roof" viewBox="0 0 464 386" aria-hidden="true">
    <polygon points="0,230 228,20 464,230 464,150 300,0 150,0 0,140" fill="#ffffff" opacity=".16"/>
    <polygon points="0,386 228,180 464,386" fill="#312d63"/>
    <polygon points="20,386 228,204 444,386" fill="#ffffff"/>
  </svg>
  <div class="brand"><span class="brand-mark"></span><span class="brand-name">Falconbright</span></div>
  <h1 class="headline"><span class="line-top">FALCONBRIGHT</span><span class="line-main">GUTTER</span><span class="line-bottom">CLEANING</span></h1>
  <p class="intro">We specialise in serving the needs of homes that want the highest standards of cleaning at very competitive rates. As a result, a high percentage of our business is from repeat customers and referrals.</p>
  <h2 class="services-title">SERVICES</h2>
  <ul class="services-list">
    <li><svg viewBox="0 0 5 7"><path d="M1 1l3 2.5L1 6" stroke="#312d63" stroke-width="1.2" fill="none"/></svg>New water fed pole systems</li>
    <li><svg viewBox="0 0 5 7"><path d="M1 1l3 2.5L1 6" stroke="#312d63" stroke-width="1.2" fill="none"/></svg>Exterior window cleaning</li>
    <li><svg viewBox="0 0 5 7"><path d="M1 1l3 2.5L1 6" stroke="#312d63" stroke-width="1.2" fill="none"/></svg>Gutter and rhone cleaning</li>
    <li><svg viewBox="0 0 5 7"><path d="M1 1l3 2.5L1 6" stroke="#312d63" stroke-width="1.2" fill="none"/></svg>Fascia and Soffit cleaning</li>
    <li><svg viewBox="0 0 5 7"><path d="M1 1l3 2.5L1 6" stroke="#312d63" stroke-width="1.2" fill="none"/></svg>Conservatory cleaning</li>
    <li><svg viewBox="0 0 5 7"><path d="M1 1l3 2.5L1 6" stroke="#312d63" stroke-width="1.2" fill="none"/></svg>One-off cleans</li>
    <li><svg viewBox="0 0 5 7"><path d="M1 1l3 2.5L1 6" stroke="#312d63" stroke-width="1.2" fill="none"/></svg>Builders cleans</li>
  </ul>
  <div class="photo-frame frame-a"><div role="img" aria-label="Gloved hand lifting autumn leaves out of a roof gutter"></div></div>
  <div class="photo-frame frame-b"><div role="img" aria-label="Red brush on a pole cleaning a white conservatory roof"></div></div>
  <div class="strapline"><span><b>Excellent Customer Service.</b></span><span><b>Competitive prices.</b></span><span><b>Established 1994.</b></span></div>
  <div class="contact">
    <p><svg viewBox="0 0 10 10"><path d="M5 .5a3 3 0 0 1 3 3c0 2.2-3 5-3 5s-3-2.8-3-5a3 3 0 0 1 3-3z" fill="#312d63"/><circle cx="5" cy="3.5" r="1.1" fill="#83aedf"/></svg>7 Old Pennick Court Harlow Street Edinburgh EH4 9RQ</p>
    <p class="phones"><svg viewBox="0 0 10 10"><path d="M2 1l2 2-1 1.2c.6 1.3 1.5 2.2 2.8 2.8L7 6l2 2-1.3 1.3C4.5 9 1 5.5.7 2.3z" fill="#312d63"/></svg>0131 482 7719, 0800 061 2287</p>
    <p><svg viewBox="0 0 10 10"><rect x=".5" y="2" width="9" height="6.5" fill="#312d63"/><path d="M.8 2.3L5 5.6l4.2-3.3" stroke="#83aedf" stroke-width=".8" fill="none"/></svg>info@falconbright-cleaning.example</p>
    <p><svg viewBox="0 0 10 10"><circle cx="5" cy="5" r="4.2" fill="none" stroke="#312d63" stroke-width=".9"/><path d="M.8 5h8.4M5 .8c-2.2 2.5-2.2 5.9 0 8.4M5 .8c2.2 2.5 2.2 5.9 0 8.4" stroke="#312d63" stroke-width=".7" fill="none"/></svg>falconbright-cleaning.example</p>
  </div>
</section>

<!-- Window side -->
<section class="flyer flyer--window">
  <div class="hero-photo" role="img" aria-label="Photo of a window cleaner with a squeegee washing a large pane of glass"></div>
  <svg class="roof" viewBox="0 0 464 386" aria-hidden="true">
    <polygon points="0,230 228,20 464,230 464,150 300,0 150,0 0,140" fill="#ffffff" opacity=".16"/>
    <polygon points="0,386 228,180 464,386" fill="#312d63"/>
    <polygon points="20,386 228,204 444,386" fill="#ffffff"/>
  </svg>
  <div class="brand"><span class="brand-mark"></span><span class="brand-name">Falconbright</span></div>
  <h1 class="headline"><span class="line-top">FALCONBRIGHT</span><span class="line-main">WINDOW</span><span class="line-bottom">CLEANING</span></h1>
  <p class="intro">We specialise in serving the needs of homes that want the highest standards of cleaning at very competitive rates. As a result, a high percentage of our business is from repeat customers and referrals.</p>
  <h2 class="services-title">SERVICES</h2>
  <ul class="services-list">
    <li><svg viewBox="0 0 5 7"><path d="M1 1l3 2.5L1 6" stroke="#312d63" stroke-width="1.2" fill="none"/></svg>New water fed pole systems</li>
    <li><svg viewBox="0 0 5 7"><path d="M1 1l3 2.5L1 6" stroke="#312d63" stroke-width="1.2" fill="none"/></svg>Exterior window cleaning</li>
    <li><svg viewBox="0 0 5 7"><path d="M1 1l3 2.5L1 6" stroke="#312d63" stroke-width="1.2" fill="none"/></svg>Gutter and rhone cleaning</li>
    <li><svg viewBox="0 0 5 7"><path d="M1 1l3 2.5L1 6" stroke="#312d63" stroke-width="1.2" fill="none"/></svg>Fascia and Soffit cleaning</li>
    <li><svg viewBox="0 0 5 7"><path d="M1 1l3 2.5L1 6" stroke="#312d63" stroke-width="1.2" fill="none"/></svg>Conservatory cleaning</li>
    <li><svg viewBox="0 0 5 7"><path d="M1 1l3 2.5L1 6" stroke="#312d63" stroke-width="1.2" fill="none"/></svg>One-off cleans</li>
    <li><svg viewBox="0 0 5 7"><path d="M1 1l3 2.5L1 6" stroke="#312d63" stroke-width="1.2" fill="none"/></svg>Builders cleans</li>
  </ul>
  <div class="photo-frame frame-a"><div role="img" aria-label="Water fed pole brush spraying, a brick house front and a squeegee on glass"></div></div>
  <div class="photo-frame frame-b"><div role="img" aria-label="Cleaner in a blue shirt washing a glass door"></div></div>
  <div class="strapline"><span><b>Excellent Customer Service.</b></span><span><b>Competitive prices.</b></span><span><b>Established 1994.</b></span></div>
  <div class="contact">
    <p><svg viewBox="0 0 10 10"><path d="M5 .5a3 3 0 0 1 3 3c0 2.2-3 5-3 5s-3-2.8-3-5a3 3 0 0 1 3-3z" fill="#312d63"/><circle cx="5" cy="3.5" r="1.1" fill="#83aedf"/></svg>7 Old Pennick Court Harlow Street Edinburgh EH4 9RQ</p>
    <p class="phones"><svg viewBox="0 0 10 10"><path d="M2 1l2 2-1 1.2c.6 1.3 1.5 2.2 2.8 2.8L7 6l2 2-1.3 1.3C4.5 9 1 5.5.7 2.3z" fill="#312d63"/></svg>0131 482 7719, 0800 061 2287</p>
    <p><svg viewBox="0 0 10 10"><rect x=".5" y="2" width="9" height="6.5" fill="#312d63"/><path d="M.8 2.3L5 5.6l4.2-3.3" stroke="#83aedf" stroke-width=".8" fill="none"/></svg>info@falconbright-cleaning.example</p>
    <p><svg viewBox="0 0 10 10"><circle cx="5" cy="5" r="4.2" fill="none" stroke="#312d63" stroke-width=".9"/><path d="M.8 5h8.4M5 .8c-2.2 2.5-2.2 5.9 0 8.4M5 .8c2.2 2.5 2.2 5.9 0 8.4" stroke="#312d63" stroke-width=".7" fill="none"/></svg>falconbright-cleaning.example</p>
  </div>
</section>

</body>
</html>
```